New Design for Water Vending Machine

Re-design graphics for face plate of water jug vending machine.

Attached are the following:
-Picture of the current face plate for the vending machine. The layout and workflow of the system have been changed.
-Picture of the new face plate without a decal installed.
-Picture of an actual installation of these vending machines for reference.
-DXF File with layout of the face plate
-PDF File with layout notes

The graphics will be printed on a lexan decal. There will be holes cutout for the following:
-Corvel Credit card reader
-Coin reject button
-Coin slot
-4 x Buttons
-Change return
Each of the cutouts should be approximately 5mm larger in all directions than the cutout size on the DXF file.

The flow of the system is as follows:
1. Insert Coins or tap Pendra/Credit/PrePaid Card
2. Press 'Format' button until desired bottle size is displayed.
3. Press 'Start' to begin filling.
'Pause' Button may be pressed during fill to switch containers or temporarily pause fill.
A poster has also been attached that is currently displayed above the prototype machines for customer reference.

Note that the bottom button is not currently used. Perhaps the design could include a window of sorts to add a label to it down the road.

The logos for TallyCoin, Orbu and Pendra Zip could be displayed near the cutout for the Corvel system.

The phrase 'Premium Drinking Water processed by Reverse Osmosis' should be displayed somewhere on the plate.

Dimensions of the face plate are 12.75" wide x 29.75" high. Dimensions of the graphics will be 10.25" x 27".

The display window will simply be clear lexan. No material will be cutout. Buffer space around display window should be 7mm.

Requirements
Must have
• Vibrant colors, and be eye catching. We want customers to be visually appealed by the machine. It should also follow a blue color theme. Text needs to be clearly layed out, and be concise.

```html
<!DOCTYPE html>
<html lang="en">
<head>
<meta charset="utf-8">
<title>Refill Machine Face Plate</title>
<link rel="stylesheet" href="https://fonts.googleapis.com/css2?family=Kanit:ital,wght@1,500;1,700&family=Montserrat+Alternates:ital,wght@1,900&family=Roboto+Condensed:ital,wght@1,500&display=swap">
<style>
  :root {
    --sky: #3ea3f0;
    --deep: #2475c9;
    --navy: #123564;
    --red: #e83a34;
    --lime: #73f040;
    --yellow: #f4ef2a;
    --white: #ffffff;
  }
  * { margin: 0; padding: 0; box-sizing: border-box; }
  html, body { width: 1200px; height: 2800px; overflow: hidden; background: var(--deep); }
  .face-plate {
    position: relative; width: 1200px; height: 2800px; overflow: hidden;
    background: radial-gradient(ellipse at 48% 45%, var(--sky) 0%, #3597e6 45%, var(--deep) 100%);
  }
  .face-plate > svg.shapes { position: absolute; inset: 0; }
  .step-text, .note, .button-label, .return-label, .tips li, .pay-name {
    position: absolute; font-family: "Kanit", sans-serif; font-style: italic;
  }
  .step-text {
    color: var(--white); font-weight: 700; font-size: 46px; line-height: 53px;
    text-shadow: 3px 3px 0 var(--navy), 0 0 6px rgba(18,53,100,.6);
    letter-spacing: -0.5px;
  }
  .step-one { left: 147px; top: 668px; }
  .step-two { left: 324px; top: 1048px; }
  .step-three { left: 241px; top: 1393px; }
  .note {
    left: 750px; top: 306px; color: var(--red); font-weight: 500;
    font-size: 26px; line-height: 32px;
  }
  .button-label {
    width: 260px; margin-left: -130px; text-align: center;
    color: var(--yellow); font-weight: 700; font-size: 46px; line-height: 50px;
    text-shadow: 3px 3px 0 var(--navy), 0 0 6px rgba(18,53,100,.6);
  }
  .label-size { left: 889px; top: 1216px; }
  .label-start { left: 889px; top: 1500px; }
  .label-pause { left: 889px; top: 1778px; }
  .pay-name {
    top: 878px; color: var(--white); font-weight: 700; font-size: 30px; line-height: 34px;
  }
  .pay-tally { left: 700px; }
  .pay-orbu { left: 868px; }
  .pay-pendra { left: 972px; top: 860px; width: 120px; text-align: center; }
  .title { position: absolute; left: 0; top: 0; }
  .title text {
    font-family: "Montserrat Alternates", sans-serif; font-style: italic; font-weight: 900;
    stroke: var(--navy); stroke-width: 14px; paint-order: stroke; stroke-linejoin: round;
  }
  .title .title-red { fill: var(--red); font-size: 200px; }
  .title .title-white { fill: var(--white); font-size: 148px; }
  .return-label {
    left: 201px; top: 2546px; color: var(--white); font-weight: 700; font-size: 42px; line-height: 50px;
    text-shadow: 3px 3px 0 var(--navy);
  }
  .tips { list-style: none; }
  .tips li {
    left: 620px; width: 500px;
    color: var(--white); font-family: "Roboto Condensed", sans-serif; font-weight: 500;
    font-size: 38px; line-height: 46.5px;
    text-shadow: 2px 2px 0 var(--navy), 0 0 5px var(--navy);
  }
  .tip-change { top: 2294px; }
  .tip-hold { top: 2433px; }
  .tip-short { top: 2573px; }
</style>
</head>
<body>
<main class="face-plate">
  <svg class="shapes" width="1200" height="2800" viewBox="0 0 1200 2800">
    <defs>
      <marker id="arrow-head" viewBox="0 0 10 10" refX="6" refY="5" markerWidth="4" markerHeight="4" orient="auto">
        <path d="M0 0 L10 5 L0 10" fill="none" stroke="#e83a34" stroke-width="2.6" stroke-linejoin="round"/>
      </marker>
    </defs>

    <g class="registration-marks" fill="var(--lime)">
      <rect x="53" y="53" width="24" height="24"/><rect x="320" y="53" width="24" height="24"/>
      <rect x="587" y="53" width="24" height="24"/><rect x="854" y="53" width="24" height="24"/>
      <rect x="1123" y="53" width="24" height="24"/>
      <rect x="53" y="349" width="24" height="24"/><rect x="1123" y="349" width="24" height="24"/>
      <rect x="53" y="646" width="24" height="24"/><rect x="1123" y="646" width="24" height="24"/>
      <rect x="53" y="942" width="24" height="24"/><rect x="1123" y="942" width="24" height="24"/>
      <rect x="53" y="1239" width="24" height="24"/><rect x="1123" y="1239" width="24" height="24"/>
      <rect x="53" y="1536" width="24" height="24"/><rect x="1123" y="1536" width="24" height="24"/>
      <rect x="53" y="1833" width="24" height="24"/><rect x="1123" y="1833" width="24" height="24"/>
      <rect x="53" y="2129" width="24" height="24"/><rect x="1123" y="2129" width="24" height="24"/>
      <rect x="53" y="2426" width="24" height="24"/><rect x="1123" y="2426" width="24" height="24"/>
      <rect x="53" y="2723" width="24" height="24"/><rect x="320" y="2723" width="24" height="24"/>
      <rect x="587" y="2723" width="24" height="24"/><rect x="854" y="2723" width="24" height="24"/>
      <rect x="1123" y="2723" width="24" height="24"/>
    </g>

    <g class="cutouts" fill="var(--lime)">
      <rect class="display-window" x="323" y="165" width="553" height="84"/>
      <circle cx="276" cy="148" r="5"/><circle cx="914" cy="148" r="5"/>
      <circle cx="276" cy="265" r="5"/><circle cx="914" cy="265" r="5"/>

      <circle class="coin-slot-ring" cx="432" cy="468" r="80" fill="var(--red)"/>
      <circle cx="376" cy="468" r="17"/><circle cx="488" cy="468" r="12"/>
      <rect x="434" y="413" width="9" height="111" rx="4"/>
      <circle cx="295" cy="468" r="11"/><circle cx="376" cy="610" r="11"/>

      <rect class="card-reader" x="734" y="408" width="315" height="391"/>
      <circle cx="734" cy="388" r="8"/><circle cx="1049" cy="388" r="8"/>
      <circle cx="797" cy="825" r="8"/><circle cx="986" cy="825" r="8"/>

      <circle cx="288" cy="1257" r="11"/><circle cx="288" cy="1586" r="11"/><circle cx="288" cy="1915" r="11"/>

      <rect class="coin-return" x="191" y="2372" width="301" height="139"/>
      <circle cx="159" cy="2441" r="7"/><circle cx="525" cy="2441" r="7"/>
    </g>

    <g class="buttons">
      <circle cx="891" cy="1136" r="57" fill="var(--lime)" stroke="var(--red)" stroke-width="22"/>
      <circle cx="891" cy="1419" r="57" fill="var(--lime)" stroke="var(--red)" stroke-width="22"/>
      <circle cx="891" cy="1701" r="57" fill="var(--lime)" stroke="var(--red)" stroke-width="22"/>
      <circle cx="891" cy="1984" r="57" fill="var(--lime)" stroke="var(--red)" stroke-width="22"/>
    </g>

    <g class="step-badges" font-family="Kanit, sans-serif" font-style="italic" font-weight="700" font-size="58" text-anchor="middle">
      <circle cx="89" cy="748" r="41" fill="var(--red)" stroke="var(--white)" stroke-width="5"/>
      <circle cx="89" cy="748" r="45" fill="none" stroke="var(--navy)" stroke-width="3"/>
      <text x="87" y="768" fill="var(--white)">1</text>
      <circle cx="264" cy="1128" r="41" fill="var(--red)" stroke="var(--white)" stroke-width="5"/>
      <circle cx="264" cy="1128" r="45" fill="none" stroke="var(--navy)" stroke-width="3"/>
      <text x="262" y="1148" fill="var(--white)">2</text>
      <circle cx="183" cy="1419" r="41" fill="var(--red)" stroke="var(--white)" stroke-width="5"/>
      <circle cx="183" cy="1419" r="45" fill="none" stroke="var(--navy)" stroke-width="3"/>
      <text x="181" y="1439" fill="var(--white)">3</text>
    </g>

    <g class="flow-arrows" fill="none" stroke="var(--red)" stroke-width="9" stroke-linecap="round" marker-end="url(#arrow-head)">
      <path d="M318 658 C300 610 310 560 348 532"/>
      <path d="M543 707 C565 660 610 640 664 652"/>
      <path d="M696 1163 C692 1200 715 1235 758 1240"/>
      <path d="M665 1457 C660 1505 720 1535 806 1528"/>
      <path d="M198 2570 C165 2565 152 2540 162 2513"/>
    </g>

    <g class="tip-dots" fill="var(--red)" stroke="var(--navy)" stroke-width="4">
      <circle cx="588" cy="2318" r="18"/><circle cx="588" cy="2457" r="18"/><circle cx="588" cy="2597" r="18"/>
    </g>
  </svg>

  <p class="note">*Credit/Debit and coin<br>combination not accepted</p>

  <p class="step-text step-one">Insert Coins<br>or tap Pendra / Credit<br>/ PrePaid Card</p>
  <p class="step-text step-two">Press 'Format' button<br>until desired bottle<br>size is displayed.</p>
  <p class="step-text step-three">Press 'Start' to begin filling.</p>

  <span class="pay-name pay-tally">TallyCoin</span>
  <span class="pay-name pay-orbu">Orbu</span>
  <span class="pay-name pay-pendra">Pendra<br>Zip</span>

  <p class="button-label label-size">Bottle Size</p>
  <p class="button-label label-start">Start</p>
  <p class="button-label label-pause">Pause</p>

  <svg class="title" width="1200" height="2800" viewBox="0 0 1200 2800" aria-label="New Refill machine Directions">
    <g transform="rotate(-8 400 1900)">
      <text class="title-red" x="135" y="1740" textLength="450" lengthAdjust="spacingAndGlyphs">New</text>
      <text class="title-red" x="135" y="1905" textLength="520" lengthAdjust="spacingAndGlyphs">Refill</text>
      <text class="title-white" x="135" y="2050" textLength="570" lengthAdjust="spacingAndGlyphs">machine</text>
      <text class="title-white" x="135" y="2180" textLength="650" lengthAdjust="spacingAndGlyphs">Directions</text>
    </g>
  </svg>

  <p class="return-label">Return of coins</p>

  <ul class="tips">
    <li class="tip-change">Exact change no longer required!<br>Machines will give change once<br>start is pressed.</li>
    <li class="tip-hold">When tapping card, please hold<br>your card in front of the reader<br>for a few seconds.</li>
    <li class="tip-short">If card is not held long enough,<br>machine says 'Transac</li>
  </ul>
</main>
</body>
</html>
```